New Business Card

We need to refresh our business cards. We designed these ourselves and we have no graphic design experience. We would like to find a new business card design that is professional and unique. We are an auto finance company. Feel free to play with the logo, but we would like to keep the eye very present on the card. Our corporate colors are green, grey, and white.
Green - RGB - 168,215,27; HEX - #AADD22
Grey - RGB - 196,196,196; HEX - #C4C4C4
Updates
Need to upload the vector file to finalize the project. The last logo was for a jpeg that didn't stretch well.
Industry/Entity Type
Financial Service
Contact Information for Business Card
Honestly don't know...I need your help!

```html
<!DOCTYPE html>
<html lang="en">
<head>
<meta charset="utf-8">
<title>Brightvale Capital — Business Card</title>
<link rel="stylesheet" href="https://fonts.googleapis.com/css2?family=Cormorant+Garamond:wght@500;600&display=swap">
<style>
  :root {
    --backdrop: #7b7b7b;
    --card: #fafafa;
    --brand-green: #aadd22;
    --brand-grey: #c4c4c4;
    --ink: #111111;
  }
  * { margin: 0; padding: 0; box-sizing: border-box; }
  html, body {
    width: 1200px;
    height: 1200px;
    overflow: hidden;
    background: var(--backdrop);
  }
  .canvas {
    position: relative;
    width: 1200px;
    height: 1200px;
  }
  .card {
    position: absolute;
    left: 219px;
    width: 768px;
    height: 464px;
    background: var(--card);
  }
  .card--front { top: 67px; }
  .card--back { top: 646px; }

  .wordmark {
    position: absolute;
    display: flex;
    align-items: center;
    font-family: "Cormorant Garamond", Georgia, serif;
    font-weight: 600;
    color: var(--brand-green);
    white-space: nowrap;
  }
  .wordmark__dot {
    border-radius: 50%;
    background: var(--brand-grey);
    flex: none;
  }
  .card--front .wordmark {
    left: 0;
    right: 0;
    top: 196px;
    justify-content: center;
    font-size: 54px;
    gap: 18px;
  }
  .card--front .wordmark__dot { width: 58px; height: 58px; }

  .card--back .wordmark {
    left: 48px;
    top: 318px;
    font-size: 34px;
    gap: 12px;
  }
  .card--back .wordmark__dot { width: 38px; height: 38px; }

  .contact {
    position: absolute;
    left: 507px;
    font-family: "Cormorant Garamond", Georgia, serif;
    font-weight: 500;
    font-size: 25px;
    line-height: 30px;
    color: var(--ink);
  }
  .contact--person { top: 40px; }
  .contact--address { top: 232px; }
  .contact--email { top: 316px; }
  .contact--web { top: 376px; }
</style>
</head>
<body>
<main class="canvas">
  <section class="card card--front" aria-label="Card front">
    <div class="wordmark"><span class="wordmark__dot"></span>Brightvale Capital</div>
  </section>

  <section class="card card--back" aria-label="Card back">
    <div class="wordmark"><span class="wordmark__dot"></span>Brightvale Capital</div>
    <p class="contact contact--person">Daniel Okafor<br>Accountant</p>
    <p class="contact contact--address">14, Palm Grove Road<br>Garki I, Abuja.</p>
    <p class="contact contact--email">dan@brightvale.com</p>
    <p class="contact contact--web">www.brightvale.com</p>
  </section>
</main>
</body>
</html>
```